Switch Kit - Banking Flyer

We want a design for an 8.5x11" flyer that matches the look of our website (www.marlowtradebank.com). Outline is attached, but please feel free to include images/pictures/graphics that you think makes this easy to understand. The goal is to hand this flyer to a potential customer to get them to understand the information easily and quickly.

```html
<!DOCTYPE html>
<html lang="en">
<head>
<meta charset="utf-8">
<title>Switch Kit – Marlow Trade Bank</title>
<link rel="stylesheet" href="https://fonts.googleapis.com/css2?family=Montserrat:wght@400;500;700;800;900&display=swap">
<style>
  :root {
    --navy: #1f3556;
    --navy-deep: #182a46;
    --navy-band: #2b4a73;
    --orange: #f7a935;
    --white: #ffffff;
    --ink: #1d3459;
  }
  * { margin: 0; padding: 0; box-sizing: border-box; }
  html, body { width: 848px; height: 1200px; overflow: hidden; background: var(--navy); }
  .flyer {
    position: relative; width: 848px; height: 1200px; overflow: hidden;
    background: linear-gradient(180deg, var(--navy) 0%, #223a5e 55%, var(--navy-deep) 100%);
    font-family: "Montserrat", sans-serif; color: var(--white);
  }
  .hero-visual {
    position: absolute; left: 0; top: 0; width: 848px; height: 1000px;
    background:
      radial-gradient(ellipse 230px 250px at 500px 360px, rgba(247,169,53,0.55), rgba(247,169,53,0) 70%),
      radial-gradient(ellipse 420px 380px at 560px 420px, rgba(120,140,170,0.35), rgba(120,140,170,0) 75%),
      radial-gradient(ellipse 380px 260px at 420px 720px, rgba(90,110,140,0.25), rgba(90,110,140,0) 75%);
  }
  .brand {
    position: absolute; left: 40px; top: 56px;
    font-weight: 700; font-size: 22px; letter-spacing: 0.5px; color: var(--white);
  }
  .headline {
    position: absolute; left: 40px; top: 330px; width: 640px;
    font-weight: 800; font-size: 41px; line-height: 54.5px; letter-spacing: -0.6px;
    text-transform: uppercase; text-shadow: 0 2px 6px rgba(0,0,0,0.3);
  }
  .step { position: absolute; left: 132px; border-left: 2px solid var(--orange); padding-left: 10px; }
  .step-title {
    color: var(--orange); font-weight: 800; font-size: 13.4px; line-height: 14.5px;
    text-transform: uppercase; letter-spacing: -0.3px; margin-bottom: 2px;
  }
  .step p { font-size: 13.2px; line-height: 17.8px; font-weight: 500; margin-bottom: 8px; }
  .step p:last-child { margin-bottom: 0; }
  .highlight { color: var(--orange); font-weight: 900; }
  .step--open { top: 600px; height: 96px; width: 380px; padding-top: 4px; }
  .step--redirect { top: 726px; height: 186px; width: 600px; padding-top: 3px; }
  .step--close { top: 947px; height: 105px; width: 620px; padding-top: 6px; }
  .step--close .step-title { margin-bottom: 8px; }
  .step-icon { position: absolute; }
  .footer-band { position: absolute; left: 0; top: 1093px; width: 848px; height: 107px; background: var(--navy-band); }
  .web-panel { position: absolute; left: 0; top: 0; width: 848px; height: 1200px; }
  .web-cta { position: absolute; left: 528px; top: 1100px; width: 300px; text-align: center; color: var(--ink); }
  .web-cta .label { font-weight: 900; font-size: 29px; line-height: 32px; letter-spacing: -0.3px; }
  .web-cta .url { font-weight: 800; font-size: 14.5px; line-height: 18px; }
  .contact { position: absolute; left: 144px; font-size: 16px; line-height: 19px; font-weight: 500; }
  .contact--address { top: 1114px; }
  .contact--phone { top: 1155px; }
  .contact-icon { position: absolute; }
</style>
</head>
<body>
<main class="flyer">
  <div class="hero-visual" role="img" aria-label="Photo of a hand holding a phone showing a bank account switching login screen, with glowing orange panels and banking icons"></div>

  <div class="brand">Marlow Trade Bank</div>

  <h1 class="headline">We look forward to creating an exceptional experience for you at Marlow Trade Bank.</h1>

  <svg class="step-icon" style="left:42px;top:610px" width="76" height="76" viewBox="0 0 76 76" aria-hidden="true">
    <path d="M22 12 A33 33 0 1 1 22 64" fill="none" stroke="#fff" stroke-width="5" stroke-linecap="round"/>
    <circle cx="13" cy="38" r="7" fill="none" stroke="#f7a935" stroke-width="4.5"/>
    <path d="M20 38 H52 M40 38 V45 M47 38 V43" fill="none" stroke="#f7a935" stroke-width="4.5" stroke-linecap="round"/>
  </svg>
  <section class="step step--open">
    <h2 class="step-title">Open a Marlow Trade Bank account</h2>
    <p>Stop by our branch and visit with our knowledgeable team to open your new account. We will be happy to assist you in choosing the right account for your banking needs.</p>
  </section>

  <svg class="step-icon" style="left:30px;top:804px" width="88" height="56" viewBox="0 0 88 56" aria-hidden="true">
    <g stroke="#fff" stroke-width="4" stroke-linecap="round">
      <path d="M12 12 H22 M4 22 H22 M12 34 H22 M4 44 H22"/>
    </g>
    <circle cx="58" cy="28" r="23" fill="none" stroke="#fff" stroke-width="4" stroke-dasharray="9 5"/>
    <circle cx="58" cy="28" r="16" fill="#f7a935"/>
    <text x="58" y="36" text-anchor="middle" font-family="Montserrat, sans-serif" font-weight="800" font-size="22" fill="#1f3556">$</text>
  </svg>
  <section class="step step--redirect">
    <h2 class="step-title">Stop using your old account and redirect your<br>automatic payments and direct deposits</h2>
    <p>It is important to remember to keep your old account open to ensure all your outstanding checks, deposits, and automatic withdrawals have cleared.</p>
    <p>We will provide you with a <span class="highlight">Payments Checklist</span> to help you determine the companies you may need to notify of your account change so they can redirect any deposits or automatic withdrawals.</p>
    <p>Our <span class="highlight">Direct Deposit Change Notification and Notification of Automatic Withdrawal Change</span> forms will easily allow companies to redirect your direct deposit(s) and automatic withdrawals to your new Marlow Trade Bank account.</p>
  </section>

  <svg class="step-icon" style="left:46px;top:966px" width="70" height="68" viewBox="0 0 70 68" aria-hidden="true">
    <path d="M35 2 L66 18 H4 Z" fill="#fff"/>
    <rect x="4" y="20" width="62" height="4" fill="#fff"/>
    <rect x="10" y="28" width="5" height="28" fill="#fff"/>
    <rect x="55" y="28" width="5" height="28" fill="#fff"/>
    <text x="35" y="52" text-anchor="middle" font-family="Montserrat, sans-serif" font-weight="800" font-size="26" fill="#f7a935">$</text>
    <rect x="2" y="60" width="66" height="5" fill="#fff"/>
  </svg>
  <section class="step step--close">
    <h2 class="step-title">Close your old account</h2>
    <p>Now you are ready to switch. We will even provide an Account Closure Authorization form to close your old account. Any remaining account balance will be transferred to your Marlow Trade Bank account.</p>
  </section>

  <div class="footer-band"></div>
  <svg class="web-panel" viewBox="0 0 848 1200" aria-hidden="true">
    <polygon points="474,1045 848,1064 848,1200 513,1200" fill="#f7a935"/>
  </svg>
  <div class="web-cta">
    <div class="label">Visit Our Website:</div>
    <div class="url">www.marlowtradebank.com</div>
  </div>

  <svg class="contact-icon" style="left:94px;top:1109px" width="26" height="32" viewBox="0 0 26 32" aria-hidden="true">
    <path d="M13 1 C6 1 1 6 1 13 C1 21 13 31 13 31 C13 31 25 21 25 13 C25 6 20 1 13 1 Z" fill="#fff"/>
    <circle cx="13" cy="12" r="4.5" fill="#2b4a73"/>
  </svg>
  <div class="contact contact--address">2740 East Harbor Crest Avenue, Suite 310<br>Linden Falls, AZ 85919</div>

  <svg class="contact-icon" style="left:94px;top:1151px" width="28" height="28" viewBox="0 0 28 28" aria-hidden="true">
    <rect x="0" y="0" width="28" height="28" rx="6" fill="#fff"/>
    <path d="M9 6 L12 10 L10 12.5 C11 15 13 17 15.5 18 L18 16 L22 19 L20 22 C13 22 6 15 6 8 Z" fill="#2b4a73"/>
  </svg>
  <div class="contact contact--phone">480.555.0148</div>
</main>
</body>
</html>
```